PLVN DRSK

We're a creative firm who connects content with clients.
I am looking to build a membership site where free users will upload content in either video, audio, written or picture format, and clients can choose to purchase said content through the site.
3 levels of membership - free users (who can upload content), paid users (who can browse and purchase content) and admin (my team, who can liaise between the two and shuffle content around and edit descriptions of that content).
Can this even be done!?

I'll just ask for a design at this stage, then once I've selected it I can work with you to progress into a fully functioning site if that works?

For paid users I would like it to have a square-tile look- similar to stoneandriver.example (although I don't like Kol-V, I much prefer Bri).

I'd like to be able to edit the site's content myself, so even if you were to design the site through something like wix? I'm new to this so let me know if I'm being ridiculus.

Target Market(s)

15-50yr old. Creatives, designers, advertisers.

Industry/Entity Type

Advertising

Number of Pages Required

5+ page

Font styles to use
Sans Serif

Requirements
Must have
• 3 levels of access/membership
• Coinvale

```html
<!DOCTYPE html>
<html lang="en">
<head>
<meta charset="utf-8">
<title>PLVN DRSK — Membership</title>
<link href="https://fonts.googleapis.com/css2?family=Roboto:wght@300;400;500;700;900&display=swap" rel="stylesheet">
<style>
:root{
  --ink:#111111;
  --dark:#121212;
  --darker:#0b0b0b;
  --topbar:#1b1b1b;
  --crimson:#9b1b30;
  --grey:#6b6b6b;
  --line:#3a3a3a;
  --white:#ffffff;
}
*{box-sizing:border-box;margin:0;padding:0}
html,body{width:1200px;height:2722px;overflow:hidden;background:var(--white)}
body{font-family:"Roboto",Arial,sans-serif;color:var(--ink)}
.page{position:relative;width:1200px;height:2722px;overflow:hidden}
.abs{position:absolute}

/* top bar */
.topbar{left:0;top:0;width:1200px;height:31px;background:var(--topbar)}
.signin{left:62px;top:7px;color:#ddd;font-size:13px;display:flex;align-items:center;gap:12px}
.search{left:1027px;top:6px;width:112px;height:19px;border-radius:10px;background:#2e2e2e;color:#666;font-size:11px;padding:3px 12px}
.search svg{position:absolute;right:8px;top:4px}

/* header */
.header{left:0;top:31px;width:1200px;height:91px;background:var(--white)}
.logo{left:60px;top:51px;font-size:44px;font-weight:900;color:var(--ink);letter-spacing:-0.5px;line-height:1}
.nav a{position:absolute;top:72px;font-size:16px;color:var(--ink);text-decoration:none;line-height:1}
.nav a.active{color:var(--crimson)}

/* hero */
.hero{left:0;top:122px;width:1200px;height:438px;
  background:radial-gradient(ellipse at 60% 40%,#a7a39a 0%,#7c7a70 35%,#4d4b40 70%,#2f2e27 100%)}
.hero-title{left:57px;top:242px;color:var(--white);font-size:48px;font-weight:300;line-height:53px}
.hero-btn{left:60px;top:386px;width:207px;height:48px;border:2px solid var(--white);border-radius:26px;color:var(--white);font-size:17px;font-weight:500;display:flex;align-items:center;justify-content:center;letter-spacing:.5px}
.hero-arrow{top:328px}

/* membership */
.section-title{left:0;width:1200px;text-align:center;font-weight:400}
.membership-title{top:576px;font-size:56px}
.section-sub{left:0;width:1200px;text-align:center;font-size:16px}
.tier{width:400px;text-align:center}
.tier-ring{position:absolute;width:142px;height:142px;border-radius:50%;border:4px solid #3a3a3a;display:flex;align-items:center;justify-content:center}
.tier-ring.free{border-color:var(--crimson)}
.tier-name{position:absolute;width:400px;text-align:center;top:853px;font-size:33px;font-weight:500}
.tier-name.free{color:var(--crimson)}
.tier-desc{position:absolute;width:400px;text-align:center;top:900px;font-size:23px;line-height:30px;color:var(--grey)}

/* content */
.content{left:0;top:1014px;width:1200px;height:228px;background:var(--dark)}
.content-title{top:1040px;font-size:56px;color:var(--white)}
.filter{top:1167px;height:36px;border:2px solid var(--white);border-radius:18px;color:var(--white);font-size:16px;display:flex;align-items:center;justify-content:center}
.filter.active{background:var(--crimson);border-color:var(--crimson)}
.tile{height:242px}
.card{left:816px;top:1251px;width:373px;height:225px;background:rgba(255,255,255,.92);padding:20px 30px 0 56px}
.card p{font-size:13.5px;line-height:23px;color:var(--ink)}
.card .date{color:var(--crimson);font-size:15px;margin-top:14px;margin-left:-4px}
.card .rule{position:absolute;left:56px;right:54px;top:172px;height:1px;background:#222}
.card .meta{position:absolute;left:56px;top:184px;font-size:16px;display:flex;align-items:center}

/* testimonial */
.testimonial-title{top:1992px;font-size:51px}
.avatar{left:535px;top:2064px;width:130px;height:130px;border-radius:50%;background:radial-gradient(circle at 50% 45%,#c59a85 0%,#7a5648 55%,#3a2a26 100%)}
.quote{left:300px;top:2234px;width:600px;text-align:center;font-size:14px;line-height:23px;color:#555}
.author{left:0;top:2295px;width:1200px;text-align:center;font-size:21px;font-weight:700;color:var(--crimson)}
.author-role{left:0;top:2331px;width:1200px;text-align:center;font-size:16px;font-weight:700}

/* footer */
.footer{left:0;top:2374px;width:1200px;height:291px;background:var(--dark)}
.foot-head{top:2416px;color:var(--white);font-size:13px;font-weight:500}
.foot-links{top:2467px;list-style:none}
.foot-links li{font-size:13px;color:var(--white);height:33px}
.foot-links li.active{color:var(--crimson)}
.newsletter-text{left:588px;top:2472px;width:250px;color:var(--white);font-size:13px;line-height:23px}
.email{left:589px;top:2527px;width:225px;height:34px;background:var(--white);font-size:12px;padding:10px 8px;color:#333}
.subscribe{left:589px;top:2582px;width:225px;height:33px;background:var(--crimson);color:var(--white);font-size:12px;display:flex;align-items:center;justify-content:center}
.socials{left:922px;top:2477px;display:flex;gap:19px}
.social-dot{width:13px;height:13px;border-radius:50%;background:var(--white)}
.social-dot.first{background:var(--crimson)}
.bottombar{left:0;top:2665px;width:1200px;height:57px;background:var(--darker)}
.bottombar span{position:absolute;top:21px;color:#ddd;font-size:12.5px}
</style>
</head>
<body>
<div class="page">

  <div class="abs topbar"></div>
  <div class="abs signin">
    <svg width="14" height="14" viewBox="0 0 14 14" aria-hidden="true"><circle cx="7" cy="4" r="3.2" fill="#777"/><path d="M1 14c0-4 3-6 6-6s6 2 6 6z" fill="#777"/></svg>
    <span>Sign In</span>
  </div>
  <div class="abs search">Search
    <svg width="11" height="11" viewBox="0 0 11 11" aria-hidden="true"><circle cx="4.5" cy="4.5" r="3.3" fill="none" stroke="#ddd" stroke-width="1.6"/><line x1="7" y1="7" x2="10.3" y2="10.3" stroke="#ddd" stroke-width="1.8"/></svg>
  </div>

  <header class="abs header"></header>
  <div class="abs logo">PlvnDrsk</div>
  <nav class="nav">
    <a class="active" style="left:565px">HOME</a>
    <a style="left:662px">ABOUT US</a>
    <a style="left:789px">CONTENT</a>
    <a style="left:913px">MEMBERSHIP</a>
    <a style="left:1065px">CONTACT</a>
  </nav>

  <section class="abs hero" role="img" aria-label="Hero photograph: woman in a brown hat standing in a misty field of wildflowers"></section>
  <h1 class="abs hero-title">Lorem ipsum dolor sit<br>amet consectetur</h1>
  <div class="abs hero-btn">START NOW</div>
  <svg class="abs hero-arrow" style="left:16px" width="16" height="26" viewBox="0 0 16 26" aria-hidden="true"><polyline points="13,3 3,13 13,23" fill="none" stroke="#ddd" stroke-width="3"/></svg>
  <svg class="abs hero-arrow" style="left:1160px" width="16" height="26" viewBox="0 0 16 26" aria-hidden="true"><polyline points="3,3 13,13 3,23" fill="none" stroke="#ddd" stroke-width="3"/></svg>

  <h2 class="abs section-title membership-title">Membership</h2>
  <p class="abs section-sub" style="top:641px">Lorem ipsum dolor sit amet consectetur adipiscing elisit amet, consectetur</p>

  <div class="tier-ring free" style="left:125px;top:698px">
    <svg width="80" height="70" viewBox="0 0 80 70" aria-hidden="true">
      <circle cx="30" cy="20" r="12" fill="#333"/><path d="M6 62c0-18 10-26 24-26s24 8 24 26z" fill="#333"/>
      <circle cx="50" cy="26" r="12" fill="#333" stroke="#fff" stroke-width="3"/><path d="M26 68c0-18 10-26 24-26s24 8 24 26z" fill="#333" stroke="#fff" stroke-width="3"/>
    </svg>
  </div>
  <div class="tier-ring" style="left:529px;top:698px">
    <svg width="64" height="46" viewBox="0 0 64 46" aria-hidden="true"><rect width="64" height="46" fill="#3a3a3a"/><text x="32" y="28" fill="#fff" font-family="Roboto, sans-serif" font-size="14" font-weight="700" text-anchor="middle">PAID</text></svg>
  </div>
  <div class="tier-ring" style="left:929px;top:698px">
    <svg width="80" height="80" viewBox="0 0 80 80" aria-hidden="true">
      <g fill="#333"><circle cx="48" cy="24" r="14"/>
      <g transform="translate(48 24)"><rect x="-3" y="-20" width="6" height="40"/><rect x="-20" y="-3" width="40" height="6"/><rect x="-3" y="-20" width="6" height="40" transform="rotate(45)"/><rect x="-3" y="-20" width="6" height="40" transform="rotate(-45)"/></g></g>
      <circle cx="48" cy="24" r="5" fill="#fff"/>
      <circle cx="32" cy="36" r="13" fill="#333" stroke="#fff" stroke-width="3"/>
      <path d="M8 76c0-18 10-26 24-26s24 8 24 26z" fill="#333" stroke="#fff" stroke-width="3"/>
    </svg>
  </div>

  <h3 class="tier-name free" style="left:-4px">Free Users</h3>
  <h3 class="tier-name" style="left:400px">Paid Users</h3>
  <h3 class="tier-name" style="left:800px">Admin</h3>
  <p class="tier-desc" style="left:-4px">Lorem ipsum dolor sit amet<br>adipiscng elit. Curitur<br>congu malesuada.</p>
  <p class="tier-desc" style="left:400px">Lorem ipsum dolor sit amet<br>adipiscng elit. Curitur<br>congu malesuada.</p>
  <p class="tier-desc" style="left:800px">Lorem ipsum dolor sit amet<br>adipiscng elit. Curitur<br>congu malesuada.</p>

  <section class="abs content"></section>
  <h2 class="abs section-title content-title">Content</h2>
  <p class="abs section-sub" style="top:1102px;color:#fff">Lorem ipsum dolor sit amet consectetur adipiscing elisit amet, consectetur</p>
  <div class="abs filter active" style="left:293px;width:105px">All</div>
  <div class="abs filter" style="left:420px;width:104px">Video</div>
  <div class="abs filter" style="left:551px;width:102px">Audio</div>
  <div class="abs filter" style="left:676px;width:106px">Written</div>
  <div class="abs filter" style="left:802px;width:103px">Picture</div>

  <div class="abs tile" style="left:0;top:1242px;width:395px;background:linear-gradient(135deg,#6d5d52,#3e3530)" role="img" aria-label="Photo: woman wearing aviator sunglasses"></div>
  <div class="abs tile" style="left:397px;top:1242px;width:406px;background:linear-gradient(135deg,#2a2a2a,#4a4440)" role="img" aria-label="Photo: tattooed hands with rings"></div>
  <div class="abs tile" style="left:805px;top:1242px;width:395px;background:linear-gradient(135deg,#7a8a96,#4f5e68)" role="img" aria-label="Photo: person in white shirt"></div>
  <div class="abs tile" style="left:0;top:1487px;width:395px;background:linear-gradient(180deg,#3d4a40,#8a6a3c 60%,#2b2a22)" role="img" aria-label="Photo: mountain lake at sunset"></div>
  <div class="abs tile" style="left:397px;top:1487px;width:406px;background:linear-gradient(135deg,#b23a58,#d78496 55%,#c9c5c3)" role="img" aria-label="Photo: close-up of pink lips and silver hair"></div>
  <div class="abs tile" style="left:805px;top:1487px;width:395px;background:linear-gradient(180deg,#8d9391,#6b5a3e 60%,#4a3f2a)" role="img" aria-label="Photo: golden dog in a grassy field"></div>
  <div class="abs tile" style="left:0;top:1731px;width:395px;background:linear-gradient(180deg,#7b8a84,#5a3e28 55%,#3c3a22)" role="img" aria-label="Photo: highland cow in a meadow"></div>
  <div class="abs tile" style="left:397px;top:1731px;width:406px;background:linear-gradient(180deg,#7d9399,#4c5448 60%,#3d4134)" role="img" aria-label="Photo: person holding a camera by a lake"></div>
  <div class="abs tile" style="left:805px;top:1731px;width:395px;background:linear-gradient(135deg,#d8b27a,#9a7240 55%,#4f6a86)" role="img" aria-label="Photo: dry grass in warm sunlight"></div>

  <article class="abs card">
    <p>Lorem ipsum dolor sit amet, consectetur adipiscing elit. Curabitur pretium congue malesuada. Aliquam ac odio a turpis luctus. Nulla tristique tempus</p>
    <p class="date">21.2.2017</p>
    <div class="rule"></div>
    <div class="meta">
      <svg width="22" height="16" viewBox="0 0 22 16" aria-hidden="true"><g stroke="#222" stroke-width="2"><line x1="0" y1="2" x2="22" y2="2"/><line x1="0" y1="6" x2="22" y2="6"/><line x1="0" y1="10" x2="22" y2="10"/><line x1="0" y1="14" x2="22" y2="14"/></g></svg>
      <span style="margin-left:34px;font-size:22px">/</span>
      <span style="margin-left:34px">Lorem ipsum</span>
    </div>
  </article>

  <h2 class="abs section-title testimonial-title">Testimonial</h2>
  <div class="abs avatar" role="img" aria-label="Portrait photo of the member giving the testimonial"></div>
  <p class="abs quote">Lorem ipsum dolor sit amet, consectetur adipiscing elit. Doanec vestibulum eros vitae ullamcorper accumsan. In vitae venenatis massa, aliquet commodo elit.</p>
  <p class="abs author">MIRA TOLVAN</p>
  <p class="abs author-role">MISSION USER FORM 2 YEARS</p>

  <footer class="abs footer"></footer>
  <h4 class="abs foot-head" style="left:86px">QUICK LINKS</h4>
  <h4 class="abs foot-head" style="left:337px">MORE LINKS</h4>
  <h4 class="abs foot-head" style="left:591px">NEWSLETTER</h4>
  <h4 class="abs foot-head" style="left:926px">FOLLOW US</h4>
  <ul class="abs foot-links" style="left:86px"><li>HOME</li><li>ABOUT US</li><li>CONTENT</li><li>MEMBERSHIP</li><li>CONTACT</li></ul>
  <ul class="abs foot-links" style="left:337px"><li class="active">AUDIO</li><li>VIDEO</li><li>WRITTEN</li><li>STORE</li><li>PICTURE</li></ul>
  <p class="abs newsletter-text">Enter your e-mail and subscribe to our newsletter</p>
  <div class="abs email">E - mail</div>
  <div class="abs subscribe">SUBSCRIBE</div>
  <div class="abs socials" aria-label="Social links">
    <span class="social-dot first"></span><span class="social-dot"></span><span class="social-dot"></span><span class="social-dot"></span><span class="social-dot"></span><span class="social-dot"></span>
  </div>

  <div class="abs bottombar">
    <span style="left:60px">Copyright © . All Rights Reserved</span>
    <span style="left:946px">Terms of Use</span>
    <span style="left:1052px">Privacy Policy</span>
  </div>

</div>
</body>
</html>
```